Visitenkarten- und Briefpapier Design - Logo vorhanden!
Zielgruppe
Wir sind eine Projektentwicklungs GmbH die Grundstücke kauft, projektiert und wieder verkauft. Eine zukünftige GmbH ist für den Innenausbau von neuen Häusern (EFH,DHH,MFH) gedacht. Wir sind ebenfalls für den Vertrieb von Häusern tätig.
Unsere Zielgruppe sind Endkunden im Immobilienbereich die Grundstücke und/oder Häuser bis Schlüsselfertig kaufen möchten, sowie Grundstückseigentümer die verkaufen wollen.
Wir benötigen Visitenkarten UND Briefpapier.
Aufgabenstellung
Bitte vorhandenes Logo verwenden.
Briefpapier:
Es soll ein ansprechendes modernes Design sein. Wir lassen uns gerne überraschen und versuchen schnellstmöglich Feedback zu geben.
Visitenkarte:
Es soll ein ansprechendes modernes Design sein. Die Visitenkarte bitte mit 2 Seiten, auf der Rückseite könnten wir uns das Dunkle ZERANT Logo sehr gut vorstellen (nur Logo).

```html
<!DOCTYPE html>
<html lang="de">
<head>
<meta charset="utf-8">
<title>ZERANT Briefpapier</title>
<link href="https://fonts.googleapis.com/css2?family=Fira+Sans:wght@300;400;500;600&display=swap" rel="stylesheet">
<style>
  :root {
    --backdrop: #ececec;
    --paper: #ffffff;
    --navy: #0f1a2b;
    --green: #6bb23a;
    --ink: #1b1b1b;
    --muted: #6a6a6a;
    --faint: #f3f3f3;
  }
  * { margin: 0; padding: 0; box-sizing: border-box; }
  html, body { width: 1200px; height: 899px; overflow: hidden; }
  body {
    background: var(--backdrop);
    font-family: "Fira Sans", sans-serif;
    color: var(--ink);
    position: relative;
  }
  .letterhead {
    position: absolute;
    left: 303px; top: 30px;
    width: 594px; height: 840px;
    background: var(--paper);
    box-shadow: 0 6px 24px rgba(0,0,0,.12);
    overflow: hidden;
  }
  .brand-block {
    position: absolute;
    left: 368px; top: 0;
    width: 166px; height: 150px;
  }
  .brand-block svg { position: absolute; inset: 0; }
  .brand-name {
    position: absolute; left: 0; right: 0; top: 58px;
    text-align: center;
    color: #ffffff;
    font-size: 22px; font-weight: 400; letter-spacing: 2px;
  }
  .fold-mark {
    position: absolute; left: 0; width: 14px; height: 1px; background: #bdbdbd;
  }
  .sender-line {
    position: absolute; left: 82px; top: 184px;
    font-size: 6.5px; letter-spacing: .3px; color: var(--ink);
  }
  .recipient {
    position: absolute; left: 82px; top: 196px;
    font-size: 10.5px; line-height: 13px; letter-spacing: .4px;
    font-style: normal;
  }
  .letter-date {
    position: absolute; right: 216px; top: 262px;
    font-size: 9.5px; letter-spacing: .2px;
  }
  .sidebar {
    position: absolute; left: 412px; top: 178px; width: 150px;
    font-size: 6px; line-height: 8px; color: var(--ink);
  }
  .sidebar-title { font-size: 8.5px; font-weight: 600; line-height: 10px; }
  .sidebar-sub { font-size: 5.5px; letter-spacing: .4px; color: var(--muted); }
  .contact-row { display: flex; gap: 5px; margin-top: 14px; align-items: flex-start; }
  .contact-row svg { flex: none; margin-top: 1px; }
  .contact-row.tight { margin-top: 3px; }
  .bank-title { font-size: 8px; font-weight: 600; margin-top: 26px; }
  .field-label { font-size: 5.5px; font-weight: 600; margin-top: 9px; }
  .field-value { font-size: 5.5px; color: var(--muted); letter-spacing: .3px; }
  .letter-body {
    position: absolute; left: 130px; top: 348px; width: 280px;
    font-size: 9.5px; line-height: 13.3px; font-weight: 400;
  }
  .salutation { margin-bottom: 14px; }
  .footer-register {
    position: absolute; left: 452px; top: 740px;
    font-size: 5.5px; line-height: 7px;
  }
  .footer-register .field-label { margin-top: 7px; color: var(--muted); }
  .faint-decoration {
    position: absolute; left: 90px; top: 700px; width: 420px; height: 140px;
    background: linear-gradient(180deg, rgba(243,243,243,0) 0%, var(--faint) 100%);
  }
</style>
</head>
<body>
  <main class="letterhead">
    <div class="faint-decoration" role="img" aria-label="Dezente Hausdach-Grafik als Hintergrundmotiv"></div>

    <div class="brand-block">
      <svg width="166" height="150" viewBox="0 0 166 150" aria-hidden="true">
        <path d="M0 0 H166 V120 C120 128 60 132 20 142 L0 148 Z" fill="var(--navy)"/>
        <path d="M0 148 L20 142 C60 132 120 128 166 120 V126 C120 134 60 138 20 146 L0 150 Z" fill="var(--green)"/>
      </svg>
      <div class="brand-name">ZERANT</div>
    </div>

    <span class="fold-mark" style="top:297px"></span>
    <span class="fold-mark" style="top:420px"></span>
    <span class="fold-mark" style="top:594px"></span>

    <div class="sender-line">ZERANT // Lindenweg 7 // D - 40213 NORDHEIM</div>
    <address class="recipient">
      ZERANT // Projektentwicklungs GmbH<br>
      Am Hang 4<br>
      40213 NORDHEIM
    </address>

    <div class="letter-date">NORDHEIM, den 18.08.2018</div>

    <aside class="sidebar">
      <div class="sidebar-title">ZERANT //</div>
      <div class="sidebar-sub">PROJEKTENTWICKLUNGS GmbH</div>

      <div class="contact-row">
        <svg width="6" height="6" viewBox="0 0 10 10"><path d="M5 0 L10 5 H8.5 V10 H1.5 V5 H0 Z" fill="var(--ink)"/></svg>
        <div>Lindenweg 7<br>D - 40213 NORDHEIM</div>
      </div>

      <div class="contact-row" style="margin-top:22px">
        <svg width="6" height="6" viewBox="0 0 10 10"><path d="M2 0 L4 2.5 L3 4 Q4.5 6.5 6 7 L7.5 6 L10 8 L8.5 10 Q2 9 0 1.5 Z" fill="var(--ink)"/></svg>
        <div>+49 (0) 555 010 30<br>+49 (0) 555 010 39</div>
      </div>

      <div class="contact-row" style="margin-top:14px">
        <svg width="6" height="6" viewBox="0 0 10 10"><circle cx="5" cy="5" r="4.5" fill="var(--ink)"/><circle cx="5" cy="5" r="2" fill="#fff"/></svg>
        <div>KONTAKT@ZERANT.de</div>
      </div>
      <div class="contact-row tight">
        <svg width="6" height="6" viewBox="0 0 10 10"><circle cx="5" cy="5" r="4.3" fill="none" stroke="var(--ink)" stroke-width="1.2"/><path d="M0.7 5 H9.3 M5 0.7 V9.3" stroke="var(--ink)" stroke-width="1"/></svg>
        <div>www.ZERANT.de</div>
      </div>

      <div class="bank-title">BANKDATEN //</div>
      <div class="field-label">IBAN</div>
      <div class="field-value">DEXX XXXX XXXX XXXX XXXX XX</div>
      <div class="field-label">BIC</div>
      <div class="field-value">XXXXXXXXXXX</div>
    </aside>

    <section class="letter-body">
      <p class="salutation">Sehr geehrte Damen und Herren,</p>
      <p>Sunt magnatem quatentiis conestis mil eum as maion num sae volore, tecte cuptasp erciis ium eaquat que niendias rendit eatem necatur re sapelesed quo blaboreperem quam int ut eatempo rectiis dolupta sperumq uasperi a volecto tota aliqui dit et excesseque laborem ipsunti tem quassit ad erchicte si dolorepe sectassit voluptate et quam autecto tatemqu asinvel estrum eum etur aborest, ommo magnimi nvernam que que dusapellabo. Itatur accaeptas dem es doluptium reperum etusam, qui nullectem sinimus, ea dolenimus est odis eriosa istis eos reptasp icipici tatectet vidus et voluptas et, ut ulpa videbistiunt estisque aut volum comnihit, volor sitibus reium, unt, eriatem aspel ipsum remquature, simperum labo. Erumque qui dolupta pos dolecestio es sitis viduciur, omnimus dolum que natur? Quiamus doloreror apitiat uritatem. Et re dolores equaernam fugiae. Mus, quidus et, optiis dollabo. Ut asped qui quunti int ommolor sum apienim odigent accum quibus ea dolore et volorem fugitaereped que pore non cum aut voluptatiis quid ullo es solorent, coris ipsant landitius dolorector aligendi omnis minus volor moluptatio. Ommolor rovitibusa sum quate non exernat uritasimenem lab ium ation none dere num dolor milis antotaquo con essi a dem etus et apition sequatum im dolut mi, tem sincide lamus, iducillit excerunt quam quam, consequis atet lanihite que reperia velessitas et volut am quamus et eicia quost, volo od maionse rferunt.</p>
    </section>

    <div class="footer-register">
      <div class="field-label" style="margin-top:0">HRB</div>
      <div class="field-value">XX XXXX XXXX XXXX XXXX XX</div>
      <div class="field-label">IHK</div>
      <div class="field-value">XXXXXXXXXXX</div>
    </div>
  </main>
</body>
</html>
```